Online trading school - Website design

We are building an online trading school (trading of shares, commodities, indices, currencies). The purpose is to teach online traders how to trade successfully. We need to design the homepage of the website and logo (bramwelloq.com will be the domain). The homepage will contain the following elements

- logo
- Sign in and Register links/buttons
- upper menu
- short introduction
- a couple of bullet points 'Why to join our school?'
- sign up form
- text
- bottom menu

Attached is a draft for the designer. The draft is just for an inspiration, the actual structure of the website can be different if the designer thinks so.

The designer is free to choose colors.

School

3 page

```html
<!DOCTYPE html>
<html lang="en">
<head>
<meta charset="utf-8">
<title>Bramwelloq – Online Trading School</title>
<link rel="stylesheet" href="https://fonts.googleapis.com/css2?family=Lato:wght@300;400;700&family=Lora:wght@400;700&display=swap">
<style>
  :root {
    --brand-blue: #0d5f8a;
    --brand-blue-dark: #0a4766;
    --brand-blue-light: #1a7aab;
    --heading-blue: #0f5b85;
    --logo-ink: #0e4d6e;
    --text: #3d3d3d;
    --text-soft: #5a5a5a;
    --section-grey: #f4f4f4;
    --field-bg: #f3f3f3;
    --field-border: #e2e2e2;
    --footer-bg: #050505;
    --white: #ffffff;
    --icon-grey: #444444;
    --footer-icon: #555555;
  }
  * { box-sizing: border-box; margin: 0; padding: 0; }
  html, body { width: 1200px; height: 2335px; overflow: hidden; }
  body {
    position: relative;
    background: var(--white);
    font-family: "Lato", Arial, sans-serif;
    color: var(--text);
  }
  .abs { position: absolute; }

  /* Header */
  .site-header { position: absolute; left: 0; top: 0; width: 1200px; height: 107px; }
  .brand-name {
    position: absolute; left: 90px; top: 32px;
    font-family: "Lato", sans-serif; font-weight: 700; font-size: 40px;
    letter-spacing: 1px; color: var(--logo-ink); line-height: 1;
  }
  .account-btn {
    position: absolute; top: 8px; height: 29px;
    background: linear-gradient(var(--brand-blue-light), var(--brand-blue-dark));
    color: var(--white); font-size: 12px; font-weight: 700; letter-spacing: .5px;
    display: flex; align-items: center; justify-content: center; border-radius: 2px;
  }
  .account-btn.sign-in { left: 892px; width: 98px; }
  .account-btn.register { left: 1008px; width: 95px; }
  .social-dot { position: absolute; border-radius: 50%; }
  .header-social .social-dot { top: 53px; width: 38px; height: 38px; background: var(--icon-grey); }

  /* Nav */
  .main-nav {
    position: absolute; left: 0; top: 107px; width: 1200px; height: 42px;
    background: linear-gradient(var(--brand-blue-light), var(--brand-blue-dark));
  }
  .main-nav ul { list-style: none; display: flex; position: absolute; left: 90px; top: 0; height: 42px; }
  .main-nav li {
    font-family: "Lora", serif; font-size: 13px; color: var(--white);
    display: flex; align-items: center; padding: 0 12px; letter-spacing: .3px;
  }
  .main-nav li.active { background: var(--brand-blue-dark); padding: 0 14px; }

  /* Hero */
  .hero { position: absolute; left: 0; top: 149px; width: 1200px; height: 541px; }
  .hero-photo {
    position: absolute; inset: 0;
    background: linear-gradient(100deg, #b9b2aa 0%, #6e6a66 35%, #2f3a4a 55%, #55575a 75%, #cfc8c0 100%);
  }
  .hero-panel {
    position: absolute; left: 0; top: 133px; width: 464px; height: 325px;
    background: rgba(0,0,0,.82); padding: 34px 0 0 89px; color: var(--white);
  }
  .hero-title { font-size: 34px; font-weight: 400; line-height: 40px; letter-spacing: 2px; }
  .hero-sub { margin-top: 16px; font-size: 22px; font-weight: 300; line-height: 27px; }
  .hero-sub strong { font-weight: 400; }
  .hero-btn {
    position: absolute; left: 89px; top: 246px; width: 191px; height: 51px;
    border: 2px solid #8fae63; color: var(--white); font-size: 21px; font-weight: 300;
    display: flex; align-items: center; justify-content: center;
  }

  /* Section headings */
  .section-title { position: absolute; font-size: 26px; font-weight: 400; color: var(--heading-blue); line-height: 1; }

  /* About */
  .about { position: absolute; left: 0; top: 690px; width: 1200px; height: 424px; background: var(--section-grey); }
  .about-text {
    position: absolute; left: 89px; top: 131px; width: 535px;
    font-size: 13.5px; line-height: 23px; color: var(--text-soft); text-align: justify;
  }
  .outline-btn {
    position: absolute; border: 2px solid var(--heading-blue); color: var(--heading-blue);
    font-size: 12px; display: flex; align-items: center; justify-content: center; background: var(--white);
  }
  .about-figure {
    position: absolute; left: 705px; top: 125px; width: 406px; height: 242px;
    background: var(--white); border: 1px solid #dcdcdc; padding: 30px 40px;
  }
  .about-figure .figure-fill {
    width: 100%; height: 100%;
    background: radial-gradient(ellipse at 55% 70%, #4aa6e8 0%, #9ccdf2 35%, #ffffff 70%);
  }

  /* Why join */
  .why-text {
    position: absolute; left: 89px; top: 1266px; width: 440px;
    font-size: 13.5px; line-height: 23px; color: var(--text-soft);
  }
  .benefits { position: absolute; left: 89px; top: 1366px; list-style: none; }
  .benefits li {
    display: flex; align-items: center; height: 32px;
    font-size: 15px; color: var(--text);
  }
  .benefits svg { width: 24px; height: 20px; margin-right: 14px; }
  .solid-btn {
    position: absolute; color: var(--white); font-weight: 700;
    background: linear-gradient(var(--brand-blue-light), var(--brand-blue-dark));
    display: flex; align-items: center; justify-content: center; border-radius: 2px;
  }
  .tour-btn { left: 89px; top: 1564px; width: 199px; height: 45px; font-size: 15px; }

  /* Join form */
  .join-form {
    position: absolute; left: 697px; top: 1211px; width: 414px; height: 398px;
    border: 2px solid #cfcfcf; background: var(--white);
  }
  .join-form h2 {
    height: 53px; margin: -2px -2px 0; padding-left: 26px;
    background: linear-gradient(var(--brand-blue-light), var(--brand-blue-dark));
    color: var(--white); font-size: 21px; font-weight: 700; display: flex; align-items: center;
  }
  .field {
    position: absolute; left: 39px; width: 336px; height: 37px;
    background: var(--field-bg); border: 1px solid var(--field-border);
    font-size: 13px; color: #8a8a8a; padding-left: 16px; display: flex; align-items: center;
  }
  .consent { position: absolute; left: 39px; top: 262px; display: flex; align-items: center; font-size: 11px; color: #8a8a8a; }
  .consent .box { width: 14px; height: 14px; border: 1px solid #c8c8c8; margin-right: 17px; background: var(--white); }
  .consent a { color: var(--heading-blue); text-decoration: none; margin-left: 3px; }
  .submit-btn {
    position: absolute; left: 39px; top: 309px; width: 336px; height: 39px;
    background: linear-gradient(#3a3a3a, #050505); color: var(--white);
    font-size: 18px; display: flex; align-items: center; justify-content: center;
  }

  /* Offers */
  .slider-arrow {
    position: absolute; top: 1727px; width: 31px; height: 31px;
    background: var(--brand-blue); display: flex; align-items: center; justify-content: center;
  }
  .offer { position: absolute; top: 1801px; width: 288px; }
  .offer-num {
    width: 54px; height: 54px; border-radius: 50%; border: 1px solid #d5d5d5;
    font-family: "Lora", serif; font-size: 27px; color: var(--heading-blue);
    display: flex; align-items: center; justify-content: center;
  }
  .offer h3 {
    margin-top: 27px; padding-bottom: 12px; border-bottom: 1px solid #e3e3e3;
    font-size: 17px; font-weight: 400; color: var(--heading-blue);
  }
  .offer p { margin-top: 11px; font-size: 13px; line-height: 17px; color: var(--text-soft); }
  .offer .plans { margin-top: 17px; }
  .offer-btn { top: 2074px; width: 120px; height: 37px; font-size: 12px; }

  /* Footer */
  .site-footer { position: absolute; left: 0; top: 2214px; width: 1200px; height: 121px; background: var(--footer-bg); }
  .footer-brand {
    position: absolute; left: 90px; top: 46px;
    font-size: 26px; font-weight: 700; letter-spacing: 1px; color: var(--white); line-height: 1;
  }
  .footer-links { position: absolute; left: 602px; top: 51px; display: flex; align-items: center; font-size: 12px; color: var(--white); }
  .footer-links .sep { margin: 0 28px; color: #aaa; }
  .footer-social .social-dot { top: 42px; width: 34px; height: 34px; background: var(--footer-icon); }
</style>
</head>
<body>

<header class="site-header">
  <div class="brand-name">BRAMWELLOQ</div>
  <a class="account-btn sign-in">SIGN IN</a>
  <a class="account-btn register">REGISTER</a>
  <div class="header-social">
    <span class="social-dot" style="left:938px" role="img" aria-label="Social network link"></span>
    <span class="social-dot" style="left:988px" role="img" aria-label="Social network link"></span>
    <span class="social-dot" style="left:1039px" role="img" aria-label="Social network link"></span>
  </div>
</header>

<nav class="main-nav">
  <ul>
    <li class="active">ABOUT OUR SCHOOL</li>
    <li>RISK WARNING</li>
    <li>TRADING GLOSSARY</li>
    <li>FAQ</li>
    <li>CONTACT US</li>
  </ul>
</nav>

<section class="hero">
  <div class="hero-photo" role="img" aria-label="Photo of a young professional sitting on a grey sofa working on a laptop"></div>
  <div class="hero-panel">
    <h1 class="hero-title">WE CAN BOOST<br>YOUR COMPANY<br>REPUTATION</h1>
    <p class="hero-sub">WITH <strong>TRUSTED PARTNERS</strong><br>KNOWN <strong>WORLD WIDE</strong></p>
    <a class="hero-btn">EXPLORE MORE</a>
  </div>
</section>

<section class="about">
  <h2 class="section-title" style="left:89px;top:78px">ABOUT COMPANY</h2>
  <p class="about-text">Lorem ipsum dolor sit amet, consectetur adipiscing elit, sed do eiusmod tempor incididunt ut labore et dolore magna aliqua. Ut enim ad minim veniam, quis nostrud exercitation ullamco laboris nisi ut aliquip ex ea commodo consequat. Duis aute irure dolor in reprehenderit in voluptate vel aute irure dolor in reprehenderit in voluptate vel aute irure dolor in reprehenderit in voluptate vel exercitation ullamco laboris nisi ut aliquip ex ea commodo consequat. Duis aute irure dolor in reprehenderit in voluptate velit esse cillum dolore eu fugiat nulla pariatur. Excepteur sint occaecat cupidatat non proident, sunt in culpa qui officia deserunt mollit anim id est laborum</p>
  <a class="outline-btn" style="left:89px;top:340px;width:95px;height:27px">Read More</a>
  <figure class="about-figure">
    <div class="figure-fill" role="img" aria-label="Illustration of business people silhouettes standing on a world map with an arrow"></div>
  </figure>
</section>

<h2 class="section-title" style="left:89px;top:1208px">WHY JOIN US?</h2>
<p class="why-text">Lorem ipsum dolor sit amet, consectetur adipiscing elit, sed do eiusmod tempor incididunt ut labore et dolore magna aliqua. Ut enim ad minim veniam, quis nostrud exercitation ullamc</p>
<ul class="benefits">
  <li><svg viewBox="0 0 24 20"><path d="M2 10 L9 17 L22 3" fill="none" stroke="#0f5b85" stroke-width="3.5"/></svg>Best trading tips ever</li>
  <li><svg viewBox="0 0 24 20"><path d="M2 10 L9 17 L22 3" fill="none" stroke="#0f5b85" stroke-width="3.5"/></svg>Secret tips from our experts</li>
  <li><svg viewBox="0 0 24 20"><path d="M2 10 L9 17 L22 3" fill="none" stroke="#0f5b85" stroke-width="3.5"/></svg>We teach you how to trade online</li>
  <li><svg viewBox="0 0 24 20"><path d="M2 10 L9 17 L22 3" fill="none" stroke="#0f5b85" stroke-width="3.5"/></svg>Learn how to trade commodities</li>
  <li><svg viewBox="0 0 24 20"><path d="M2 10 L9 17 L22 3" fill="none" stroke="#0f5b85" stroke-width="3.5"/></svg>Learn how to become a trader</li>
</ul>
<a class="solid-btn tour-btn">TAKE A TOUR</a>

<form class="join-form">
  <h2>JOIN OUR SCHOOL NOW!</h2>
  <div class="field" style="top:85px">First Name</div>
  <div class="field" style="top:141px">Last Name</div>
  <div class="field" style="top:196px">Email Address</div>
  <div class="consent"><span class="box"></span>Confirm that you are agree with <a>Terms &amp; Conditions</a></div>
  <div class="submit-btn">SUBMIT</div>
</form>

<h2 class="section-title" style="left:89px;top:1732px">WHAT WE OFFER TO YOU?</h2>
<span class="slider-arrow" style="left:1041px"><svg width="10" height="14" viewBox="0 0 10 14"><path d="M8 1 L2 7 L8 13" fill="none" stroke="#fff" stroke-width="2.5"/></svg></span>
<span class="slider-arrow" style="left:1080px"><svg width="10" height="14" viewBox="0 0 10 14"><path d="M2 1 L8 7 L2 13" fill="none" stroke="#fff" stroke-width="2.5"/></svg></span>

<article class="offer" style="left:89px">
  <div class="offer-num">1</div>
  <h3>BEST SAVING PLANS</h3>
  <p>exercitation ullamco laboris nisi ut aliquip ex ea commodo consequat. Duis aute irure dolor in reprehenderit in voluptate velit esse cillum dolore</p>
  <p class="plans">Tax Saving Plans<br>Life Saving Plans</p>
</article>
<article class="offer" style="left:457px">
  <div class="offer-num">2</div>
  <h3>FINANCIAL PLANNING</h3>
  <p>exercitation ullamco laboris nisi ut aliquip ex ea commodo consequat. Duis aute irure dolor in reprehenderit in voluptate velit esse cillum dolore</p>
  <p class="plans">Tax Saving Plans<br>Life Saving Plans</p>
</article>
<article class="offer" style="left:825px">
  <div class="offer-num">3</div>
  <h3>STUDY FEE PLANNING</h3>
  <p>exercitation ullamco laboris nisi ut aliquip ex ea commodo consequat. Duis aute irure dolor in reprehenderit in voluptate velit esse cillum dolore</p>
  <p class="plans">Tax Saving Plans<br>Life Saving Plans</p>
</article>
<a class="solid-btn offer-btn" style="left:89px">LEARN MORE</a>
<a class="solid-btn offer-btn" style="left:457px">LEARN MORE</a>
<a class="solid-btn offer-btn" style="left:825px">LEARN MORE</a>

<footer class="site-footer">
  <div class="footer-brand">BRAMWELLOQ</div>
  <div class="footer-links"><span>Terms &amp; Consitions</span><span class="sep">|</span><span>Privacy Policy</span></div>
  <div class="footer-social">
    <span class="social-dot" style="left:982px" role="img" aria-label="Social network link"></span>
    <span class="social-dot" style="left:1030px" role="img" aria-label="Social network link"></span>
    <span class="social-dot" style="left:1078px" role="img" aria-label="Social network link"></span>
  </div>
</footer>

</body>
</html>
```